Brochure for Community-Based Therapy Company

Will be given out to patients, doctors, case managers. We are redesigning our marketing materials and would like a design for a brochure. We provide therapy to individuals who have been injured in car accidents or on the job. We provide occupational therapy, speech therapy and psychotherapy. We would like the brochure to utilize our corporate ID and color scheme that we are using for our other materials (see attached letterhead and logo).

Stock photos that are used should stay away from images of outpatient or hospital settings, stay away from photos with obvious disabilities (wheelchairs, learning to walk, etc), and nothing that looks like physical therapy, as we don't provide physical therapy only OT, Speech and psychotherapy. Would prefer to not have people wearing masks, as we will use this beyond the pandemic. Also, our staff wears business casual clothing so would prefer photos that the individuals are not wearing scrubs or other medical attire (lab coats, etc).

Target Market(s)

Patients, Physicians/Doctors, Case Managers

Industry/Entity Type

Healthcare

Requirements
Must have
• Prefer a booklet format but doesn't have to be 8.5 inch by 11 inch (can be a little smaller).

```html
<!DOCTYPE html>
<html lang="en">
<head>
<meta charset="utf-8">
<title>Northfield Therapy Partners – Brochure</title>
<link rel="stylesheet" href="https://fonts.googleapis.com/css2?family=Montserrat:wght@400;600;700&family=Open+Sans:wght@400;600;700&display=swap">
<style>
:root{
  --sage:#76a594;
  --sage-dark:#5f8e7d;
  --sage-tint:#dbe9e3;
  --ink:#4a4a4a;
  --muted:#777;
  --grey-band:#5d5d60;
  --grey-panel:#e3e3e3;
  --paper:#ffffff;
  --bg:#e2e2e4;
}
*{box-sizing:border-box;margin:0;padding:0}
html,body{width:1200px;height:3096px;overflow:hidden}
body{background:var(--bg);font-family:"Open Sans",Arial,sans-serif;color:var(--ink)}
.scene{height:774px;display:flex;align-items:center;justify-content:center}
.spread{width:1060px;height:690px;display:flex;box-shadow:0 14px 40px rgba(0,0,0,.18)}
.page{position:relative;width:530px;height:690px;background:var(--paper);overflow:hidden;padding:34px 34px 60px}
.page.left{border-right:1px solid #e6e6e6}
h2,h3,h4,.brand{font-family:"Montserrat",Arial,sans-serif}
h3{color:var(--sage);font-size:14px;font-weight:700;margin:10px 0 5px}
p{font-size:8.6px;line-height:1.55;margin-bottom:6px}
ul{list-style:none}
li{font-size:8.6px;line-height:1.5;padding-left:14px;position:relative;margin-bottom:3px}
li::before{content:"";position:absolute;left:0;top:3px;width:7px;height:7px;border:1.3px solid var(--sage);border-radius:2px}
.brand{color:var(--sage);font-weight:700;letter-spacing:.5px;display:flex;align-items:center;gap:8px}
.brand .dot{width:10px;height:10px;border-radius:50%;background:var(--sage)}
/* footer */
.foot{position:absolute;left:34px;right:34px;bottom:22px;display:flex;align-items:center;gap:10px}
.foot .brand{font-size:10px}
.foot .rule{flex:1;height:1px;background:#ccc}
.foot .url{font-size:8px;background:#eee;color:var(--muted);padding:3px 10px;border-radius:10px}
.foot .num{width:22px;height:22px;border-radius:50%;background:var(--sage);color:#fff;font-size:9px;font-weight:700;display:flex;align-items:center;justify-content:center}
.photo{border-radius:2px}
/* covers */
.back-cover{background:var(--sage);padding:0;border-top:30px solid #eee;border-bottom:30px solid #eee}
.back-cover .contact{position:absolute;left:50px;right:50px;top:360px;color:#fff}
.back-cover .brand{color:#fff;font-size:16px;justify-content:center;margin-bottom:14px}
.back-cover .brand .dot{background:#fff}
.back-cover h4{text-align:center;font-size:15px;margin-bottom:16px}
.contact-cols{display:flex;gap:24px;font-size:10px;line-height:1.8}
.contact-cols div{flex:1}
.ic{display:inline-block;width:10px;height:10px;vertical-align:-1px;margin-right:6px}
.front-cover{padding:0}
.front-cover .brand{position:absolute;top:46px;right:40px;font-size:22px}
.front-cover .hero{position:absolute;top:120px;left:40px;right:0;height:320px;background:linear-gradient(135deg,#e9e1d8,#cdb9a6 55%,#8d8f9b)}
.front-cover .band{position:absolute;top:440px;left:0;right:0;bottom:30px;background:var(--sage);color:#fff;text-align:center;padding:26px 30px}
.band h2{font-weight:400;font-size:30px;letter-spacing:1px}
.band h3{color:#fff;font-size:15px;margin:8px 0 18px;line-height:1.4}
.band .url-box{display:inline-block;border:2px solid #fff;padding:8px 26px;font-family:"Montserrat",sans-serif;font-weight:700;font-size:15px}
/* inner */
.side-band{background:var(--grey-band);color:#ddd;padding:10px 14px;margin:-34px -34px 12px 120px;font-size:8px;line-height:1.5}
.factor{display:flex;gap:10px;margin-bottom:6px}
.factor .ring{flex:0 0 26px;height:26px;border-radius:50%;border:2px solid var(--sage);display:flex;align-items:center;justify-content:center}
.factor h4{color:var(--sage);font-size:11px;margin-bottom:2px}
.panel{background:var(--grey-panel);padding:14px 18px;margin-top:10px}
.panel h4{text-align:center;color:var(--sage);font-size:12px;margin-bottom:8px}
.cols{display:flex;gap:20px}
.cols ul{flex:1}
.cols li{font-weight:600}
.green-panel{background:var(--sage-tint);padding:14px 18px;margin:8px -34px 10px}
.pill{display:block;width:max-content;margin:0 auto 8px;background:var(--grey-band);color:#fff;font-size:9px;font-weight:700;padding:3px 14px;border-radius:10px}
.row{display:flex;gap:14px}
.row>*{flex:1}
.closing-art{position:absolute;top:160px;left:0;right:0;bottom:0;background:radial-gradient(circle at 50% 45%,#f2c27a 0%,#b98a78 25%,#8fa3b8 55%,#dfe6ee 85%)}
.back-page .brand{position:absolute;top:60px;right:40px;font-size:22px}
</style>
</head>
<body>

<!-- Spread 1: covers -->
<section class="scene">
 <div class="spread">
  <article class="page left back-cover">
   <div class="contact">
    <div class="brand"><span class="dot"></span>NORTHFIELD THERAPY PARTNERS</div>
    <h4>Contact Us</h4>
    <div class="contact-cols">
     <div>
      <p style="font-size:10px"><svg class="ic" viewBox="0 0 10 10"><path d="M2 1l2 2-1 1.5a6 6 0 0 0 2.5 2.5L7 6l2 2-1.5 1.5C4 9 1 6 .5 2z" fill="#fff"/></svg>555-014-2210 / 555-014-2211</p>
      <p style="font-size:10px"><svg class="ic" viewBox="0 0 10 10"><rect x="0" y="2" width="10" height="7" fill="#fff"/><path d="M0 2l5 4 5-4" stroke="#76a594" fill="none"/></svg>intake@northfield-therapy.com</p>
      <p style="font-size:10px"><svg class="ic" viewBox="0 0 10 10"><circle cx="5" cy="5" r="4.5" fill="none" stroke="#fff"/></svg>www.northfield-therapy.com</p>
     </div>
     <div>
      <p style="font-size:10px"><svg class="ic" viewBox="0 0 10 10"><path d="M5 0a3.5 3.5 0 0 1 3.5 3.5C8.5 6 5 10 5 10S1.5 6 1.5 3.5A3.5 3.5 0 0 1 5 0z" fill="#fff"/></svg>1200 Maple Ridge Drive, Suite 300, Lakeview, MI 48000</p>
      <p style="font-size:10px"><b>Office Hours:</b> Monday – Friday<br>9:00 am – 4:30 pm</p>
      <p style="font-size:10px"><b>Therapy Hours:</b> By Appointment</p>
     </div>
    </div>
   </div>
  </article>
  <article class="page front-cover">
   <div class="brand"><span class="dot"></span>NORTHFIELD THERAPY PARTNERS</div>
   <div class="hero photo" role="img" aria-label="Photo of a smiling older woman stretching a resistance band while a young therapist assists her at home"></div>
   <div class="band">
    <h2>WE PROVIDE</h2>
    <h3>OCCUPATIONAL THERAPY, SPEECH THERAPY<br>AND PSYCHOTHERAPY</h3>
    <span class="url-box">www.northfield-therapy.com</span>
   </div>
  </article>
 </div>
</section>

<!-- Spread 2: pages 01–02 -->
<section class="scene">
 <div class="spread">
  <article class="page left">
   <div class="side-band">Our team brings therapy into the places where daily life happens, helping each person return to home, work and community.</div>
   <h3>Who We Are</h3>
   <p>For over 25 years our company has provided community based rehabilitation to people recovering from injury. We work where our clients live, work and learn, so skills gained in therapy carry directly into everyday routines and lasting independence.</p>
   <h3>Finding success in the rehabilitation process relies on certain key factors:</h3>
   <div class="factor"><span class="ring"></span><div><h4>Getting to Know You</h4><p>We take time to learn your history, goals, family and daily routine before any plan is written.</p></div></div>
   <div class="factor"><span class="ring"></span><div><h4>Comprehensive Evaluation</h4><p>Our clinicians assess thinking, communication, emotional health and daily skills in your own setting.</p></div></div>
   <div class="factor"><span class="ring"></span><div><h4>Creating and Implementing a Customized Rehabilitation Plan</h4><p>After evaluation we design a plan built around your priorities, reviewed often with you and your team.</p></div></div>
   <div class="factor"><span class="ring"></span><div><h4>Focus on Accomplishments (Breaking Down Success)</h4><p>Large goals are divided into small steps so progress is visible, measurable and encouraging.</p></div></div>
   <div class="foot"><span class="brand"><span class="dot"></span>NORTHFIELD</span><span class="rule"></span><span class="url">www.northfield-therapy.com</span><span class="num">01</span></div>
  </article>
  <article class="page">
   <h3>Why Our Approach to Brain Injury is Unique</h3>
   <p>In many traditional settings therapy takes place in a clinic, far from the tasks a person must manage each day. Skills practiced there often fail to transfer to home, school or work, leaving gaps in recovery.</p>
   <p>Community based treatment closes that gap. Sessions happen in the home, workplace or neighborhood, where real demands and real distractions shape every exercise and every success.</p>
   <p>Our therapists work closely with physicians, case managers and families so that each step supports the next and every client moves steadily toward greater independence.</p>
   <h3>Who We Serve</h3>
   <ul>
    <li>We treat adults and adolescents with a variety of diagnoses. We service home and community locations throughout the region.</li>
    <li>Our therapists hold a variety of certifications and endorsements including brain injury specialist credentials.</li>
   </ul>
   <div class="panel">
    <h4>Diagnoses can Include</h4>
    <div class="cols">
     <ul><li>Traumatic Brain Injury</li><li>Postconcussional Syndrome</li><li>Spinal Cord Injury</li><li>Post-traumatic Stress Disorder</li><li>Depression</li><li>Anxiety</li></ul>
     <ul><li>Mood Disorders</li><li>Visual Impairments</li><li>Balance Disorders</li><li>Movement Disorders</li><li>Neuromuscular Pathologies</li><li>Dysphagia</li></ul>
    </div>
    <ul><li>Musculoskeletal/Orthopedic injuries (ie. Spinal fractures/pathology, nerve injuries, pain)</li></ul>
   </div>
   <div class="foot"><span class="rule"></span><span class="url">www.northfield-therapy.com</span><span class="num">02</span></div>
  </article>
 </div>
</section>

<!-- Spread 3: pages 03–04 -->
<section class="scene">
 <div class="spread">
  <article class="page left">
   <div class="row">
    <div>
     <h3>Funding Sources Include</h3>
     <ul><li>No-Fault Auto Insurance</li><li>Workers Compensation Insurance</li><li>Some Commercial Health Insurance Carriers</li></ul>
    </div>
    <div class="photo" style="height:150px;background:linear-gradient(135deg,#5a6b7c,#c9a48a 60%,#e8ddd2)" role="img" aria-label="Photo of a therapist and client working together at a table"></div>
   </div>
   <h3>Services Offered</h3>
   <h4 style="font-size:11px;margin-bottom:4px">Speech Language Pathology</h4>
   <div class="row">
    <div>
     <p>Speech language pathologists help clients regain communication and thinking skills needed for home, work and social life.</p>
     <div class="photo" style="height:190px;background:linear-gradient(135deg,#efe9e2,#cbb7a3 55%,#a9b3b8)" role="img" aria-label="Photo of a therapist guiding an older man through a tabletop activity"></div>
    </div>
    <div>
     <h4 style="font-size:10px;color:var(--sage);margin-bottom:4px">Services Include</h4>
     <ul>
      <li>Evaluation of speech, language and cognition</li>
      <li>Attention and memory training</li>
      <li>Problem solving and reasoning</li>
      <li>Word finding and expression</li>
      <li>Reading and written language</li>
      <li>Social communication skills</li>
      <li>Voice and fluency treatment</li>
      <li>Swallowing assessment</li>
      <li>Use of compensatory strategies</li>
      <li>Dysarthria and apraxia</li>
     </ul>
    </div>
   </div>
   <div class="foot"><span class="brand"><span class="dot"></span>NORTHFIELD</span><span class="rule"></span><span class="url">www.northfield-therapy.com</span><span class="num">03</span></div>
  </article>
  <article class="page">
   <h3>Occupational Therapy</h3>
   <p>Occupational therapists evaluate how injury affects daily activities and help clients rebuild the skills, habits and routines that matter most to them, from self care to returning to work.</p>
   <div class="green-panel">
    <span class="pill">Services include</span>
    <ul>
     <li>Treatment of visual, perceptual and sensory deficits</li>
     <li>Teach use of memory and organization compensation tools</li>
     <li>Assist in developing schedules and daily routines</li>
     <li>Instruct clients and family members in safe techniques</li>
     <li>Recommend home and workplace modifications</li>
     <li>Assist in reducing fatigue and managing energy</li>
     <li>Provide training in meal preparation and home tasks</li>
     <li>Provide cognitive retraining during real activities</li>
     <li>Assist with shopping, banking and community errands</li>
     <li>Facilitate driving and transportation planning</li>
     <li>Consult with employers on return to work needs</li>
    </ul>
   </div>
   <h3>Psychological and Counseling</h3>
   <div class="row">
    <ul><li>Individual &amp; Family Counseling related to the injury</li></ul>
    <ul><li>Psychological services are provided as needed and prescribed by the physician to:</li></ul>
   </div>
   <div class="foot"><span class="rule"></span><span class="url">www.northfield-therapy.com</span><span class="num">04</span></div>
  </article>
 </div>
</section>

<!-- Spread 4: page 05 and back page -->
<section class="scene">
 <div class="spread">
  <article class="page left">
   <h3>Psychological services are provided as needed and prescribed by the physician to:</h3>
   <div class="row">
    <ul><li>Address emotional needs of the patient</li><li>Provide individual and family support</li><li>Assist with adjustment to injury</li></ul>
    <ul><li>Address changes in mood and behavior</li><li>Support coping and stress management</li></ul>
   </div>
   <h3>Vocational Services</h3>
   <p>Vocational specialists help clients return to meaningful work through planning, training and close contact with employers.</p>
   <ul>
    <li>Vocational evaluation and interest testing</li>
    <li>Job site analysis and accommodations</li>
    <li>Job seeking skills and placement</li>
    <li>Return to work coordination</li>
    <li>Educational planning and support</li>
    <li>Consultation with employers and schools</li>
   </ul>
   <div class="photo" style="height:230px;margin-top:10px;background:linear-gradient(135deg,#f4f4f4,#d9d6d2 50%,#8a8c90)" role="img" aria-label="Photo of a counselor talking with a client seated in a bright room with a plant"></div>
   <div class="foot"><span class="brand"><span class="dot"></span>NORTHFIELD</span><span class="rule"></span><span class="url">www.northfield-therapy.com</span><span class="num">05</span></div>
  </article>
  <article class="page back-page" style="padding:0">
   <div class="brand"><span class="dot"></span>NORTHFIELD THERAPY PARTNERS</div>
   <div class="closing-art" role="img" aria-label="Illustration of open hands holding a glowing globe against a sunset sky"></div>
  </article>
 </div>
</section>

</body>
</html>
```